Affiliate website design and wireframe

We need a design of an affiliate website for an application we purchased, it is important that you build the website pages according to the developer of the applications specifications (please see attached documents) the developer of the application will configure the pages and add them to the site. Please take special note of his comments below.

We all so need you to create a wire frame so the developer can test everything (http://sketchwire.tolvaro.vn/)

It will be the homepage and about 16 inner pages (please see attached files)
Here is our website http://bluvendmarket.com/affiliate/affiliates/index.php

The version of the software we purchased is the Kivo Partner Hubline version

Comments from the developers

1. I will need the source files of the design (photoshop .psd files and font files if custom fonts are used), since the implementation is closely bound to component sizes (like border width, margin width etc.) and colors. If you own a corporate design manual, it's crucial to send it as well. Also, please, make sure if you use custom fonts, that these allow legal website integration (like google web fonts).

2. Any and every content is controlled via templates. All editing/adding/removing etc. is done here. The template files are essentially html/php documents, they use a template engine called quillo (http://www.quillo.net/) which has it's own language similar to php.

3. .psd files are ideal, because we deal with the specifics of KPX/KPH implementation on a daily basis. Any html/css developed in advance may prove to be a poor choice. You may choose to let an in-house developer do the job, but experience wise this is more costly, since he will not be accustomed to the template/functionality systems of KPX/KPH.

4. I will need the source files of the design (photoshop .psd files and font files if custom fonts are used), since the implementation is closely bound to component sizes (like border width, margin width etc.) and colors. If you own a corporate design manual, it's crucial to send it as well. Also, please, make sure if you use custom fonts, that these allow legal website integration (like google web fonts).

Regards,

Dorek Hanval
Multimedia Design

We prefer illustrations more than pictures of real people.

This is the home page, it is asking for Merchant and Affiliate sign up, not just affiliate.

http://bluvendmarket.com/affiliate/index.php

Please note the home page features both Merchant and Affiliate sign up

We are looking for illustration design not just stock images

Please remember the search menu that searches for the available programs, see the example we gave you, look at the search menu at the top of the page http://www.tradelumo.com/

We are reviewing everything, no need to send more designs

Target Market(s)

Natural Products Manufacturers
Natural products Sales reps
Natural Products Bloggers
Social Marketing

Industry/Entity Type

Software

Requirements
Must have
• 1. All links on pages should go to the appropriate pages.
2. Colors can be based on our logo design (look at the attachments)
3. Here is our website http://bluvendmarket.com/affiliate/affiliates/index.php
4. We have attached a drawing of how we think the homepage concept should follow.
5. Main concept of design, is trying to show our sales people (Affiliates) are doing multiple things to advertise and sell the merchants products.(see logo)
6. Need to be able to edit all text and images.
7. Our target audience is Natural product sales people (Advertisers, bloggers, ext) and natural product manufacturers.
8. You can speak to the company who made the application, through live chat, on there website http://www.kivopartnerhubline.com/
Nice to have
• See Attached Documents.
site should take up whole website pages
Look For fun Illustrated Website, one of the better ones we have seen is http://www.tradelumo.com/index.cfm
Should not have
• Please look very carefully at developers comment above.

```html
<!DOCTYPE html>
<html lang="en">
<head>
<meta charset="utf-8">
<title>BluVend Market – Affiliate Network</title>
<link href="https://fonts.googleapis.com/css2?family=Open+Sans:ital,wght@0,400;0,600;0,700;1,400&family=Oswald:wght@400;500;600&family=Roboto+Condensed:wght@400;700&display=swap" rel="stylesheet">
<style>
:root{
  --navy:#0f3166;
  --blue:#1c4a85;
  --blue-btn:#2f6db5;
  --green:#5a9e1a;
  --green-dark:#2f6b0d;
  --green-bright:#8cc63f;
  --text:#333;
  --muted:#666;
  --light:#f2f2f2;
  --dark:#1d1d1d;
  --band:#20242b;
}
*{box-sizing:border-box;margin:0;padding:0}
html,body{width:1200px;height:3019px;overflow:hidden}
body{font-family:"Open Sans",Arial,sans-serif;color:var(--text);background:#fff;position:relative}
a{color:inherit;text-decoration:none}
.wrap{width:920px;margin:0 auto;position:relative}

.topbar{height:40px;background:#fff;border-bottom:1px solid #e5e5e5;font-size:13px}
.topbar .wrap{display:flex;justify-content:space-between;align-items:center;height:40px}
.topbar nav a{margin-right:26px;color:#444}
.topbar .logins{display:flex;align-items:center;height:40px}
.topbar .logins a{margin-left:26px;color:#444}
.search-btn{width:46px;height:40px;background:var(--green);display:flex;align-items:center;justify-content:center;margin-left:20px}

.header{height:121px;background:#fff}
.header .wrap{display:flex;align-items:center;justify-content:space-between;height:121px}
.brand{display:flex;align-items:center;gap:10px;font-family:"Oswald",sans-serif;font-weight:600;font-size:26px;color:var(--green-dark);letter-spacing:.5px}
.brand .mark{width:26px;height:26px;background:var(--navy)}
.mainnav{display:flex;gap:34px;font-family:"Roboto Condensed",sans-serif;font-weight:700;font-size:15px;color:#222}

.hero{height:523px;position:relative;background:linear-gradient(180deg,#3a6aa8 0%,#2a5791 55%,#1d4377 100%);overflow:hidden}
.hero-art{position:absolute;inset:0}
.hero h1{position:absolute;left:237px;top:30px;font-family:"Oswald",sans-serif;font-weight:500;font-size:40px;line-height:48px;color:#fff;letter-spacing:.5px}
.hero h1 span{display:block;color:var(--green-bright);margin-left:100px}
.step{position:absolute;font-family:"Roboto Condensed",sans-serif;font-weight:700;font-size:16px;color:#fff;text-transform:uppercase}
.step i{position:absolute;width:38px;height:38px;border-radius:50%;background:var(--green);border:3px solid #fff;color:#fff;font-style:normal;display:flex;align-items:center;justify-content:center;font-size:17px}
.figure{position:absolute;left:560px;top:190px;width:180px;height:333px;border-radius:90px 90px 0 0;background:linear-gradient(180deg,#8fb1d8,#5d86b8)}

.livechat{position:absolute;right:0;top:340px;width:40px;height:146px;background:var(--green);border-radius:4px 0 0 4px;color:#fff;font-family:"Oswald",sans-serif;font-size:15px;writing-mode:vertical-rl;transform:rotate(180deg);display:flex;align-items:center;justify-content:center;letter-spacing:1px}

.signup{margin-top:41px;display:flex;height:211px;position:relative}
.signup .panel{flex:1;padding:22px 24px;color:#fff}
.signup .aff{background:var(--green)}
.signup .mer{background:var(--blue)}
.signup h2{font-family:"Roboto Condensed",sans-serif;font-weight:700;font-size:22px;margin-bottom:10px}
.signup p{font-size:14px;line-height:21px}
.signup .btn{display:inline-block;margin:22px 0 0 126px;padding:12px 22px;font-family:"Roboto Condensed",sans-serif;font-weight:700;font-size:16px;color:#fff}
.aff .btn{background:var(--green-dark)}
.mer .btn{background:var(--blue-btn);margin-left:128px}
.or{position:absolute;left:50%;top:50%;transform:translate(-50%,-50%);width:50px;height:50px;border-radius:50%;background:var(--blue);border:3px solid #fff;color:#fff;font-family:"Roboto Condensed",sans-serif;font-weight:700;font-size:16px;display:flex;align-items:center;justify-content:center}

.welcome{text-align:center;padding-top:60px;height:252px}
.section-title{font-family:"Roboto Condensed",sans-serif;font-weight:700;font-size:31px;line-height:38px;color:var(--navy);text-transform:uppercase}
.welcome p{font-size:12.5px;line-height:21px;color:#333;margin-top:14px}

.success{height:292px;background:linear-gradient(180deg,#2a2f37,#1a1d22);color:#fff;text-align:center;padding-top:70px}
.success h2{font-family:"Roboto Condensed",sans-serif;font-weight:700;font-size:30px;letter-spacing:.5px}
.success p{font-family:"Oswald",sans-serif;font-weight:400;font-size:26px;line-height:38px;margin-top:18px;text-transform:uppercase;letter-spacing:.5px}

.services{height:405px;text-align:center;padding-top:38px;overflow:hidden}
.service-grid{display:flex;justify-content:space-between;margin-top:28px}
.service{width:210px}
.service .icon{width:120px;height:120px;border-radius:50%;background:#e9e9e9;margin:0 auto;display:flex;align-items:center;justify-content:center}
.service h3{font-family:"Roboto Condensed",sans-serif;font-weight:700;font-size:14px;color:var(--navy);margin-top:14px;line-height:20px;height:40px}
.service p{font-size:13px;line-height:21px;color:#444;margin-top:6px;height:84px;overflow:hidden}
.service a{display:block;font-size:13px;line-height:21px;color:#333;margin-top:4px}

.cta{height:279px;background:linear-gradient(180deg,#4b6e33,#3a5a26);text-align:center;color:#fff;padding-top:72px}
.cta h2{font-family:"Roboto Condensed",sans-serif;font-weight:700;font-size:30px}
.cta a{display:inline-block;margin-top:22px;border:2px solid #fff;padding:9px 24px;font-family:"Oswald",sans-serif;font-size:22px;letter-spacing:.5px}

.testimonial{text-align:center;padding-top:50px;height:296px}
.testimonial blockquote{position:relative;font-style:italic;font-size:14px;line-height:23px;color:#666;margin:30px auto 0;width:720px}
.testimonial blockquote::before,.testimonial blockquote::after{position:absolute;font-family:Georgia,serif;font-size:70px;color:#ddd;font-style:normal}
.testimonial blockquote::before{content:"\201C";left:-50px;top:-20px}
.testimonial blockquote::after{content:"\201D";right:-34px;bottom:-60px}
.divider{width:920px;margin:0 auto;border-top:1px solid #e3e3e3}

.clients{text-align:center;padding-top:40px;height:250px}
.client-row{display:flex;justify-content:space-between;margin-top:28px}
.client{width:170px;height:78px;border:1px solid #ddd;display:flex;align-items:center;justify-content:center;gap:8px;font-family:"Roboto Condensed",sans-serif;font-weight:700;font-size:17px;color:#333}
.client .dot{width:12px;height:12px;border-radius:50%;background:#333}

.footer{position:absolute;left:0;top:2710px;width:1200px;height:309px;background:var(--dark);color:#ddd}
.foot-cols{display:flex;padding-top:36px}
.foot-col{font-size:12.5px;line-height:25px}
.foot-col h4{font-family:"Roboto Condensed",sans-serif;font-weight:700;font-size:15px;color:#fff;margin-bottom:8px}
.c1{width:250px}.c2{width:278px}.c3{width:272px}
.badge{width:118px;height:40px;border:1px solid #777;border-radius:6px;background:#000;margin-bottom:10px}
.social{display:flex;gap:8px;margin-top:14px}
.social span{width:30px;height:30px;border-radius:50%;background:#fff}
.foot-bottom{position:absolute;left:140px;right:140px;top:250px;border-top:1px solid #333;padding-top:14px;display:flex;justify-content:space-between;font-size:12px;color:#bbb}
.foot-bottom nav a{margin-left:40px}
</style>
</head>
<body>

<div class="topbar">
  <div class="wrap">
    <nav><a href="#">Home</a><a href="#">About</a><a href="#">Faq</a><a href="#">Contact Us</a></nav>
    <div class="logins"><a href="#">Affiliate Login</a><a href="#">Merchant Login</a>
      <a class="search-btn" href="#" aria-label="Search"><svg width="20" height="20" viewBox="0 0 20 20"><circle cx="8" cy="8" r="6" fill="none" stroke="#fff" stroke-width="2.5"/><line x1="12.5" y1="12.5" x2="18" y2="18" stroke="#fff" stroke-width="3"/></svg></a>
    </div>
  </div>
</div>

<header class="header">
  <div class="wrap">
    <a class="brand" href="#"><span class="mark"></span>BLUVEND MARKET</a>
    <nav class="mainnav"><a href="#">SEARCH FOR MEARCHANTS</a><a href="#">OFFERS</a><a href="#">FEATURES</a><a href="#">TESTIMONIALS</a><a href="#">PARTNERS</a></nav>
  </div>
</header>

<section class="hero">
  <div class="hero-art" role="img" aria-label="Illustration of a cheerful salesman holding a tablet, surrounded by affiliate steps with icons over a city crowd background"></div>
  <div class="figure" role="img" aria-label="Illustrated affiliate salesman character"></div>
  <h1>EARNING MONEY AS A<span>BLUVEND MARKET</span></h1>
  <div class="step" style="left:325px;top:250px">Join Affiliates<i style="left:110px;top:-96px">1</i></div>
  <div class="step" style="left:165px;top:390px">Find Product<i style="left:90px;top:-94px">2</i></div>
  <div class="step" style="left:360px;top:482px">Promote Product<i style="left:18px;top:-82px">3</i></div>
  <div class="step" style="left:768px;top:482px">Track Sale<i style="left:22px;top:-100px">4</i></div>
  <div class="step" style="left:878px;top:318px">Earn Commisions<i style="left:112px;top:-110px">5</i></div>
</section>

<a class="livechat" href="#">LIVE CHAT</a>

<div class="wrap signup">
  <div class="panel aff">
    <h2>FOR AFFILIATES</h2>
    <p>Lorem ipsum dolor sit amet, consectetur adipiscing elit. Aenean pretium porttitor est, sed laoreet urna molestie quis. Cras tincidunt consectetur nulla sed mollis.</p>
    <a class="btn" href="#">AFFILIATES SIGNUP</a>
  </div>
  <div class="panel mer">
    <h2>FOR MERCHANTS</h2>
    <p>Lorem ipsum dolor sit amet, consectetur adipiscing elit. Aenean pretium porttitor est, sed laoreet urna molestie quis. Cras tincidunt consectetur nulla sed mollis.</p>
    <a class="btn" href="#">MERCHANT SIGNUP</a>
  </div>
  <div class="or">OR</div>
</div>

<section class="wrap welcome">
  <h2 class="section-title">Welcome to BluVend Market</h2>
  <p>Lorem Ipsum is simply dummy text of the printing and typesetting industry. Lorem Ipsum has been the industry's standard dummy text ever since the 1500s, when an unknown printer took a galley of type and scrambled it to make a type specimen book. It has survived not only five centuries, but also the leap into electronic typesetting, remaining essentially unchanged. It was popularised in the 1960s with the release Lorem Ipsum passages, and more recently with desktop publishing software like Pagewright Studio including versions of Lorem Ipsum.</p>
</section>

<section class="success" role="img" aria-label="Dark band with silhouettes of business people">
  <h2>MAXIMIZE YOUR SUCCESS WITH BLUVEND MARKET</h2>
  <p>Let our industry-leading digital marketing platform power your<br>earnings in ways you never dreamed possible.</p>
</section>

<section class="wrap services">
  <h2 class="section-title">Our Services</h2>
  <div class="service-grid">
    <div class="service">
      <div class="icon"><svg width="54" height="60" viewBox="0 0 54 60"><path d="M20 4h14l-5 10h-4z" fill="#0f3166"/><path d="M22 16h10c12 8 20 20 20 30 0 9-7 13-25 13S2 55 2 46c0-10 8-22 20-30z" fill="#0f3166"/><text x="27" y="48" text-anchor="middle" fill="#fff" font-family="Open Sans,sans-serif" font-weight="700" font-size="22">$</text></svg></div>
      <h3>Earn up to 50% Commission<br>for all Products</h3>
      <p>Not only can you join our team and help spread the word about your favorite...</p>
      <a href="#">[Read More]</a>
    </div>
    <div class="service">
      <div class="icon"><svg width="50" height="58" viewBox="0 0 50 58"><g fill="#0f3166"><ellipse cx="25" cy="8" rx="23" ry="7"/><path d="M2 14c0 4 10 7 23 7s23-3 23-7v10c0 4-10 7-23 7S2 28 2 24z"/><path d="M2 30c0 4 10 7 23 7s23-3 23-7v10c0 4-10 7-23 7S2 44 2 40z"/><path d="M2 46c0 4 10 7 23 7s23-3 23-7v4c0 4-10 7-23 7S2 54 2 50z"/></g></svg></div>
      <h3>High Conversion Rate =<br>More Money</h3>
      <p>Our website and plans generate one of the highest conversion rates in the industry...</p>
      <a href="#">[Read More]</a>
    </div>
    <div class="service">
      <div class="icon"><svg width="64" height="50" viewBox="0 0 64 50"><g fill="#0f3166"><ellipse cx="32" cy="24" rx="24" ry="18"/><path d="M16 10l-2-10 12 6z"/><rect x="52" y="18" width="10" height="10" rx="3"/><rect x="18" y="36" width="8" height="13"/><rect x="38" y="36" width="8" height="13"/></g><rect x="26" y="10" width="12" height="3" fill="#fff"/></svg></div>
      <h3>Long cookie<br>duration</h3>
      <p>If a customer comes from your site to ours, and then comes back to purchase six...</p>
      <a href="#">[Read More]</a>
    </div>
    <div class="service">
      <div class="icon"><svg width="56" height="56" viewBox="0 0 56 56"><circle cx="28" cy="28" r="25" fill="none" stroke="#0f3166" stroke-width="5"/><text x="28" y="40" text-anchor="middle" fill="#0f3166" font-family="Open Sans,sans-serif" font-weight="700" font-size="34">?</text></svg></div>
      <h3>How does it<br>work?</h3>
      <p>It couldn't be simpler! We've streamlined our entire affiliate process to ensure ease...</p>
      <a href="#">[Read More]</a>
    </div>
  </div>
</section>

<section class="cta" role="img" aria-label="Green band with a faded office desk scene">
  <h2>READY TO GET STARTED?</h2>
  <a href="#">SIGN UP NOW</a>
</section>

<section class="wrap testimonial">
  <h2 class="section-title">Our Happy Clients Say</h2>
  <blockquote>Lorem Ipsum is simply dummy text of the printing and typesetting industry. Lorem Ipsum has been the industry's standard dummy text ever since the 1500s, when an unknown printer took a galley of type and scrambled it to make a type specimen book. It has survived not only five centuries, but also the leap into electronic typesetting, remaining essentially unchanged.</blockquote>
</section>
<div class="divider"></div>

<section class="wrap clients">
  <h2 class="section-title">Our Clients Are Featured In</h2>
  <div class="client-row">
    <div class="client"><span class="dot"></span>Meridan Electric</div>
    <div class="client">Fojiro</div>
    <div class="client">Altrona Air</div>
    <div class="client">Panvera</div>
    <div class="client">Arqel</div>
  </div>
</section>

<footer class="footer">
  <div class="wrap foot-cols">
    <div class="foot-col c1"><h4>ABOUT US</h4><a href="#">Company</a><br><a href="#">Contact us</a><br><a href="#">Privacy Policy</a></div>
    <div class="foot-col c2"><h4>AFFILIATES</h4><a href="#">Affiliates information</a><br><a href="#">Affiliate link formats</a></div>
    <div class="foot-col c3"><h4>MERCHANTS</h4><a href="#">Merchants Login</a><br><a href="#">Integration methods</a><br><a href="#">API Reference</a><br><a href="#">Samples and Tests</a><br><a href="#">Kivo Partner Pro</a></div>
    <div class="foot-col"><h4>MOBILE</h4><div class="badge"></div><div class="badge"></div><div class="social"><span></span><span></span><span></span></div></div>
  </div>
  <div class="foot-bottom"><span>Copyright © 2014, BluVend Market.All Right reserved.</span><nav><a href="#">Terms and Conditions</a><a href="#">Intergration</a></nav></div>
</footer>

</body>
</html>
```